Eyecatcher-Broschüre für Hochzeitsfotografen
Perfekte und sehr angenehme Zusammenarbeit, bei der das optimale Ergebnis im Fokus stand. Super Einsatz - vielen Dank dafür!
Zielgruppe
Hochzeitsfotograf aus Köln / fotografiert deutschlandweit exklusive Hochzeitsreportagen
Zielgruppe: moderne Paare, designorientiert, offen, fotobegeistert mit dem Blick für das besondere Foto, welches die Geschichte ihres Hochzeitstages erzählt. Paare, die einen Künstler suchen und keinen Dienstleister !
Aufgabenstellung
Format DIN A5 oder DIN A4 - zwei erste Entwurfseiten füge ich als PDF bei, so dass man schon eine Idee erhält, wie ich es mir vorstellen kann. Ich bin aber offen für Neues.
Weniger ist Mehr!
puristische Gestaltung ohne viele Schnörkel - aber zeitgemäß und aktuell - Broschüre sollte maximal 8 Seiten haben - Lust auf mehr sollte durch eine aussergewöhnliche Broschüre entstehen.
Bild & Textmaterial kann für den Entwurf von meiner Webseite verwendet werden: jorisklaff-brautbilder.de

```html
<!DOCTYPE html>
<html lang="de">
<head>
<meta charset="utf-8">
<title>Broschüre – Doppelseite stilvoll</title>
<link rel="stylesheet" href="https://fonts.googleapis.com/css2?family=Arimo:wght@400&family=Libre+Baskerville:wght@400&display=swap">
<style>
  :root {
    --backdrop: #ddd6d1;
    --paper: #fbfbfb;
    --ink: #6f6f6f;
    --ink-soft: #9a9a9a;
    --circle: #d9d9d9;
    --bouquet-pink: #e9a9c6;
    --bouquet-magenta: #c8438f;
    --bouquet-white: #f4f2ee;
    --dress: #ece8e4;
    --mono-dark: #3a3a3a;
    --mono-light: #d8d8d8;
  }
  * { box-sizing: border-box; margin: 0; padding: 0; }
  html, body { width: 1200px; height: 829px; overflow: hidden; }
  body { background: var(--backdrop); display: flex; align-items: center; justify-content: center; }

  .spread {
    width: 990px; height: 700px;
    display: flex;
    box-shadow: 0 10px 30px rgba(80, 60, 50, 0.18);
  }
  .page { width: 495px; height: 700px; background: var(--paper); position: relative; }

  .page--left .bouquet-photo {
    position: absolute; inset: 0;
    background:
      radial-gradient(circle at 30% 45%, var(--bouquet-pink) 0 12%, transparent 26%),
      radial-gradient(circle at 62% 62%, var(--bouquet-pink) 0 10%, transparent 24%),
      radial-gradient(circle at 70% 42%, var(--bouquet-magenta) 0 5%, transparent 14%),
      radial-gradient(circle at 45% 68%, var(--bouquet-magenta) 0 4%, transparent 12%),
      radial-gradient(circle at 50% 40%, var(--bouquet-white) 0 18%, transparent 36%),
      radial-gradient(ellipse at 48% 52%, #8da77a 0 20%, transparent 45%),
      linear-gradient(180deg, #e6cbbd 0%, var(--dress) 30%, #f1eeeb 100%);
  }
  .page--right::before {
    content: ""; position: absolute; left: 0; top: 0; bottom: 0; width: 60px;
    background: linear-gradient(90deg, rgba(0,0,0,0.08), transparent);
  }

  .intro {
    position: absolute; left: 34px; top: 44px; width: 140px;
    font-family: "Arimo", Arial, sans-serif; font-size: 9px; line-height: 1.35;
    color: var(--ink);
  }
  .detail-photo {
    position: absolute; left: 255px; top: 130px; width: 215px; height: 215px;
    background:
      radial-gradient(ellipse at 75% 35%, var(--mono-light) 0 20%, transparent 45%),
      linear-gradient(115deg, var(--mono-dark) 0%, #8a8a8a 40%, var(--mono-light) 70%, #f0f0f0 100%);
  }
  .motto {
    position: absolute; right: 40px; top: 470px;
    font-family: "Libre Baskerville", Georgia, serif; font-size: 20px;
    color: var(--ink);
  }
  .folio {
    position: absolute; left: 30px; bottom: 34px;
    display: flex; align-items: center; gap: 20px;
    font-family: "Arimo", Arial, sans-serif; font-size: 10px; color: var(--ink-soft);
  }
  .folio__number {
    width: 26px; height: 26px; border-radius: 50%;
    background: var(--circle); color: #fff;
    display: flex; align-items: center; justify-content: center; font-size: 11px;
  }
</style>
</head>
<body>
  <main class="spread">
    <section class="page page--left">
      <div class="bouquet-photo" role="img" aria-label="Brautstrauß mit rosa Pfingstrosen, weißen Blüten und Schleierkraut vor weißem Brautkleid"></div>
    </section>
    <section class="page page--right">
      <p class="intro">Meine Bilder sind hell und fokussiert. Durch meinen langjährigen Background in der Fashion- und Beauty-Fotografie, ähneln meine Aufnahmen Beautyportraits und zeigen Euch und Eure Lieben in wunderbarem Licht.</p>
      <div class="detail-photo" role="img" aria-label="Schwarzweißfoto: Hände schließen die Knopfleiste eines bestickten Brautkleids"></div>
      <p class="motto">stilvoll</p>
      <footer class="folio">
        <span class="folio__number">11</span>
        <span class="folio__couple">Carla &amp; Jonas</span>
      </footer>
    </section>
  </main>
</body>
</html>
```